business card - Helicopter Flight Services, Flight School, etc.

We need a business card design for a new helicopter service.

We offer Helicopter Flight Services, Aerial Filming & Photography, Flight School, and Helicopter Tours. In that order.

Summit BladeLine, Inc.
Harold Tebbets
SummitBladeline@Mailvane.com
555-014-2786

Based at the Corvell Airport in Van Nuys, CA. The final design should communicate integrity and safety. Pictures or logos at your discretion.

Card back side - surprise me.

```html
<!DOCTYPE html>
<html lang="en">
<head>
<meta charset="utf-8">
<title>Summit BladeLine, Inc. — Business Card</title>
<link rel="stylesheet" href="https://fonts.googleapis.com/css2?family=Michroma&family=Open+Sans:wght@400;600;700&display=swap">
<style>
  :root {
    --backdrop: #2b2d31;
    --card: #ffffff;
    --brand-blue: #1e8cf0;
    --rotor-grey: #8e8e8e;
    --ink: #1c1c1c;
    --art-light: #cfe5fb;
  }
  * { box-sizing: border-box; margin: 0; padding: 0; }
  html, body {
    width: 1200px;
    height: 864px;
    overflow: hidden;
    background: var(--backdrop);
  }
  .canvas {
    width: 1200px;
    height: 864px;
    display: flex;
    flex-direction: column;
    align-items: center;
    justify-content: center;
    gap: 40px;
  }
  .card {
    position: relative;
    width: 600px;
    height: 343px;
    background: var(--card);
    overflow: hidden;
    box-shadow: 0 10px 30px rgba(0,0,0,0.35);
  }

  /* Front side */
  .card--front {
    display: flex;
    flex-direction: column;
    align-items: center;
    justify-content: center;
    gap: 40px;
  }
  .brand-mark {
    display: flex;
    align-items: center;
    gap: 14px;
    margin-top: 10px;
  }
  .brand-mark__dot {
    width: 30px;
    height: 30px;
    border-radius: 50%;
    background: var(--brand-blue);
  }
  .brand-mark__name {
    font-family: "Michroma", sans-serif;
    font-size: 21px;
    color: var(--brand-blue);
    letter-spacing: 0.5px;
    text-transform: uppercase;
  }
  .services {
    font-family: "Open Sans", sans-serif;
    font-size: 15px;
    color: var(--ink);
    text-align: center;
    line-height: 1.5;
  }
  .services__row { display: flex; justify-content: center; align-items: center; gap: 10px; }
  .services__sep {
    width: 7px; height: 7px; border-radius: 50%;
    background: var(--brand-blue);
  }

  /* Back side */
  .back-title {
    position: absolute;
    left: 30px;
    top: 20px;
    font-family: "Michroma", sans-serif;
    font-weight: 400;
    font-size: 23px;
    line-height: 1.3;
    color: var(--brand-blue);
    letter-spacing: 1.5px;
  }
  .contact {
    position: absolute;
    left: 34px;
    top: 178px;
    font-family: "Open Sans", sans-serif;
  }
  .contact__name {
    font-weight: 700;
    font-size: 19px;
    color: var(--brand-blue);
    margin-bottom: 20px;
  }
  .contact__line {
    display: flex;
    align-items: center;
    gap: 10px;
    font-size: 15px;
    color: var(--ink);
    margin-bottom: 5px;
  }
  .contact__icon { width: 13px; height: 13px; fill: var(--brand-blue); flex: none; }
  .back-art {
    position: absolute;
    right: 0;
    bottom: 0;
    width: 330px;
    height: 240px;
    border-top-left-radius: 160px 120px;
    background: linear-gradient(160deg, var(--rotor-grey) 0%, var(--art-light) 35%, var(--brand-blue) 100%);
  }
</style>
</head>
<body>
<main class="canvas">
  <section class="card card--front" aria-label="Card front">
    <div class="brand-mark">
      <span class="brand-mark__dot"></span>
      <span class="brand-mark__name">Summit BladeLine, Inc.</span>
    </div>
    <div class="services">
      <div class="services__row">
        <span>Helicopter Flight Services</span><span class="services__sep"></span><span>Aerial Filming &amp; Photography</span>
      </div>
      <div class="services__row">
        <span>Flight School</span><span class="services__sep"></span><span>Helicopter Tours</span>
      </div>
    </div>
  </section>

  <section class="card card--back" aria-label="Card back">
    <div class="back-art" role="img" aria-label="Large helicopter artwork with blue rotor ring and grey blade, cropped at the card corner"></div>
    <h1 class="back-title">SUMMIT<br>BLADELINE,<br>INC.</h1>
    <div class="contact">
      <p class="contact__name">Harold Tebbets</p>
      <p class="contact__line">
        <svg class="contact__icon" viewBox="0 0 24 24" aria-hidden="true"><path d="M6.6 10.8a15.1 15.1 0 0 0 6.6 6.6l2.2-2.2a1 1 0 0 1 1-.25 11.4 11.4 0 0 0 3.6.57 1 1 0 0 1 1 1V20a1 1 0 0 1-1 1A17 17 0 0 1 3 4a1 1 0 0 1 1-1h3.5a1 1 0 0 1 1 1c0 1.25.2 2.45.57 3.57a1 1 0 0 1-.25 1z"/></svg>
        555-014-2786
      </p>
      <p class="contact__line">
        <svg class="contact__icon" viewBox="0 0 24 24" aria-hidden="true"><path d="M2 5h20v14H2z M2 5l10 7 10-7"/></svg>
        SummitBladeline@Mailvane.com
      </p>
    </div>
  </section>
</main>
</body>
</html>
```